Summit Pharmacy Coral Gate Shopping Centre Light Box

We have the opportunity of having a very large External Light Box (Visible area - 5.7 Meters Wide by 8.4 Meters High) on the outside of the shopping center (Coral Gate Shopping Center) where our Store (Summit Pharmacy) is Located to display for a 5 month period.
Coral Gate shopping center is a premier shopping destination in the Gold Coast, Queensland, Australia. The Gold Coast is the premier holiday/tourist destination in Australia (Sun, Surf beaches, Palm trees and theme parks abound).
Coral Gate shopping center is currently undergoing a major redevelopment, which required us (Summit Pharmacy) to close for 10 months. Now we have re-opened (in a corner of the center 1st to be redeveloped), we need to let our old (and new) customers know we're back open. We also have a medical center (Medics@Coral Gate) located within our Chemist.
Please see the attached files, which show the look of our store, our Logo, the medical center logo, an image (that may be a useful guideline for an image? - green depicting a bottle and leaf - nature), as well as (most importantly) a file entitled "Light Box Coral Gate.oxps which shows pictures of the actual light box (the one with the guy holding the surfboard) that we are to obtain.
We really are looking for a combination of the right image, together with the words “Summit Pharmacy Coral Gate Now Open” (probably using our logo) and then include the words “incorporating “Medics@Coral Gate Medical Centre” (maybe using their logo). It's that simple.
Probably the other criteria for the job would be
- Longevity – the creative should be able to last throughout the campaign period without losing its appeal over time
- A creative that fits within the environment (Gold Coast, lifestyle, etc.)
- A creative that can stand up on its own and doesn’t get lost sitting next to the Velmora creative or other potential advertisers
"Please note one learning from the Velmora creative is that the font should have been larger. One bit of advice we received from the printer/installer was to provide one strong image and keep the copy short/to the point- similar to the Quill ads noted with Hawthorne- this was a simple yet powerful campaign."
Thank You,
Mark Dorrell
PLEASE NOTE: we are after very little wording.
Essentially just "Summit Pharmacy Coral Gate Now Open, incorporating "Medics @ Coral Gate (Bulk Billing Medical Centre)
Ground floor alongside TK Sound or Just inside this entrance ...... or similar.
The best file attachment to look at to get a feel for this job is the "light box Coral Gate" file as this shows pictures of exactly where it's going to go and how large etc.
With regards to the overall look, we're looking for "less is more" on an image, with the small amount of wording similar to that mentioned above.
The image could be a lifestyle/beach type image, or a health/family type image, or something similar to the green image we have in the files depicting naturopathy.

• Green is our store colour - PMS 375

• Our Green. PMS 375 and suitable image,
• Logo/name LARGE

```html
<!DOCTYPE html>
<html lang="en">
<head>
<meta charset="utf-8">
<title>Summit Pharmacy Coral Gate Light Box</title>
<link rel="stylesheet" href="https://fonts.googleapis.com/css2?family=Montserrat:wght@500;800&display=swap">
<style>
  :root {
    --panel-black: #050505;
    --ink-white: #ffffff;
    --soft-grey: #cfcfcf;
    --vial-pink: #e8327c;
    --drop-cyan: #27c4e8;
  }
  * { margin: 0; padding: 0; box-sizing: border-box; }
  html, body { width: 910px; height: 1200px; overflow: hidden; background: var(--panel-black); }
  .lightbox {
    position: relative;
    width: 910px;
    height: 1200px;
    background: var(--panel-black);
    font-family: "Montserrat", Arial, sans-serif;
    color: var(--ink-white);
  }
  .hero-art {
    position: absolute;
    left: 250px;
    top: 110px;
    width: 460px;
    height: 520px;
    border-radius: 50%;
    background: radial-gradient(ellipse at 60% 35%, rgba(232,50,124,0.55) 0%, rgba(39,196,232,0.22) 40%, rgba(5,5,5,0) 72%);
  }
  .headline {
    position: absolute;
    left: 0;
    right: 0;
    top: 720px;
    text-align: center;
    font-weight: 800;
    font-size: 48px;
    line-height: 1.2;
    letter-spacing: 1px;
    text-transform: uppercase;
  }
  .details {
    position: absolute;
    left: 0;
    right: 0;
    top: 930px;
    text-align: center;
    font-weight: 500;
    font-size: 20px;
    line-height: 1.5;
    color: var(--soft-grey);
  }
  .partner-row {
    position: absolute;
    left: 60px;
    right: 60px;
    bottom: 70px;
    display: flex;
    justify-content: space-between;
    align-items: center;
  }
  .brand-name {
    display: flex;
    align-items: center;
    gap: 12px;
    font-weight: 800;
    font-size: 22px;
    color: var(--ink-white);
  }
  .brand-dot {
    width: 34px;
    height: 34px;
    border-radius: 50%;
    background: var(--ink-white);
  }
</style>
</head>
<body>
  <main class="lightbox">
    <div class="hero-art" role="img" aria-label="Pink glass vial tipping over, spilling pink, cyan and white droplets"></div>

    <h1 class="headline">Summit Pharmacy<br>Coral Gate<br>Now Open</h1>

    <p class="details">Incorporating Medics@Coral Gate Medical Centre<br>Ground floor alongside TK Sound</p>

    <footer class="partner-row">
      <div class="brand-name"><span class="brand-dot"></span>Summit Pharmacy</div>
      <div class="brand-name"><span class="brand-dot"></span>Medics@Coral Gate</div>
    </footer>
  </main>
</body>
</html>
```